Business Card Design Project

We are a construction company in Orange County, CA. We need a two sided business card. We would like the back to be our logo with web URL. Front should included Name, title, address, phone, fax and email address.

our address is
387 West Marlowe Blvd, Suite 402
Fairhaven, CA 90412

Our logo files are attached.

Construction

```html
<!DOCTYPE html>
<html lang="en">
<head>
<meta charset="utf-8">
<title>Varden Business Card</title>
<link href="https://fonts.googleapis.com/css2?family=Open+Sans:wght@400;700;800&display=swap" rel="stylesheet">
<style>
  :root {
    --brand-blue: #184a7c;
    --ink: #3b3f45;
    --muted: #7a7f86;
    --card: #ffffff;
    --backdrop: #ece9e4;
    --rule: #b9bcc0;
  }
  * { margin: 0; padding: 0; box-sizing: border-box; }
  html, body { width: 1200px; height: 444px; overflow: hidden; }
  body {
    background: var(--backdrop);
    font-family: "Open Sans", Arial, sans-serif;
    position: relative;
  }
  .card {
    position: absolute;
    top: 75px;
    width: 515px;
    height: 294px;
    background: var(--card);
    border-radius: 16px;
    overflow: hidden;
    box-shadow: 0 3px 8px rgba(0,0,0,0.25);
  }
  .card--front { left: 67px; }
  .card--back { left: 618px; }

  .wordmark {
    position: absolute;
    left: 0; right: 0;
    text-align: center;
    color: var(--brand-blue);
    font-weight: 800;
    font-size: 60px;
    letter-spacing: -0.5px;
    line-height: 1;
  }
  .card--front .wordmark { top: 40px; }
  .card--back .wordmark { top: 98px; }

  .identity {
    position: absolute;
    top: 172px; left: 0; right: 0;
    display: flex;
    justify-content: center;
    align-items: center;
    gap: 7px;
  }
  .identity__name { font-weight: 700; font-size: 17px; color: var(--brand-blue); }
  .identity__divider { width: 1px; height: 24px; background: var(--rule); }
  .identity__title { font-size: 13px; color: var(--muted); }

  .contacts {
    position: absolute;
    top: 224px; left: 0; right: 0;
    display: flex;
    justify-content: center;
    gap: 12px;
    font-size: 12.5px;
    color: var(--ink);
    white-space: nowrap;
  }
  .contact { display: flex; align-items: center; gap: 3px; }
  .contact svg { width: 10px; height: 10px; fill: var(--brand-blue); }

  .band-rule {
    position: absolute;
    left: 0; right: 0;
    bottom: 39px;
    height: 3px;
    background: linear-gradient(90deg, #d9dbde, var(--rule) 50%, #d9dbde);
  }
  .band {
    position: absolute;
    left: 0; right: 0; bottom: 0;
    height: 39px;
    background: var(--brand-blue);
    color: #fff;
    display: flex;
    align-items: center;
    justify-content: center;
    font-size: 13.5px;
  }
  .card--back .band { font-size: 12.5px; letter-spacing: 2px; }
</style>
</head>
<body>
  <section class="card card--front">
    <div class="wordmark">VARDEN</div>
    <div class="identity">
      <span class="identity__name">YOUR NAME</span>
      <span class="identity__divider"></span>
      <span class="identity__title">Title</span>
    </div>
    <div class="contacts">
      <span class="contact">
        <svg viewBox="0 0 10 10"><path d="M2 0.5 L4 2.8 L3 4 Q4 6 6 7 L7.2 6 L9.5 8 L8 9.5 Q4 9.5 0.5 2 Z"/></svg>
        0912345678
      </span>
      <span class="contact">
        <svg viewBox="0 0 10 10"><rect x="2" y="0.5" width="6" height="3"/><rect x="0.5" y="4" width="9" height="4" rx="1"/><rect x="2" y="7" width="6" height="2.5"/></svg>
        0923456781
      </span>
      <span class="contact">
        <svg viewBox="0 0 10 10"><rect x="0.5" y="2" width="9" height="6"/></svg>
        info@vardenco.com
      </span>
      <span class="contact">
        <svg viewBox="0 0 10 10"><circle cx="5" cy="5" r="4.5"/></svg>
        www.vardenco.com
      </span>
    </div>
    <div class="band-rule"></div>
    <div class="band">387 West Marlowe Blvd, Suite 402 Fairhaven, CA 90412</div>
  </section>

  <section class="card card--back">
    <div class="wordmark">VARDEN</div>
    <div class="band-rule"></div>
    <div class="band">www.vardenco.com</div>
  </section>
</body>
</html>
```